Quick Straightforward Billboard Redesign

- Design billboard sized for 10 foot' x 36' foot width live area size and please include bleeds 6" around all sides
- Exact blue color match is imperative in headline, logo, phone number bubble or wherever used. C-83 / M-45 / Y-1 / K-0-
- What I hope to illustrate is that our company offers the best porch screening in the area area, in regards to quality, expertise, durability, storms proof, but we do not build screen porches.
- Current board is attached below from previous designer, and as you can see sizing was off, white space on edges make it appear to be sized incorrectly.
- I also attached my own little mock up idea well well if it helps, favorite image, logo, headline, etc and ideas perhaps on expanding or making this better?

Thanks so much!

Target Market(s)

Drivers and passengers, Southeastern NC, are of immense new construction and high end homes.

Industry/Entity Type

Construction

Colors
0054AA
0677BA
7BADD7
CADEEF
E8F1F8

Requirements
Must have
• Blue color matching
Nice to have
• Design spins or other thoughts on my little mock up

```html
<!DOCTYPE html>
<html lang="en">
<head>
<meta charset="utf-8">
<title>Harborview Screening Billboard</title>
<link rel="stylesheet" href="https://fonts.googleapis.com/css2?family=Bebas+Neue&family=Montserrat:wght@800&display=swap">
<style>
  :root {
    --brand-blue: #006db8;
    --brand-green: #00b95f;
    --paper: #ffffff;
    --ink-light: #ffffff;
    --photo-light: #e6e8ea;
    --photo-warm: #d3c9ba;
  }
  * { margin: 0; padding: 0; box-sizing: border-box; }
  html, body { width: 1200px; height: 357px; overflow: hidden; background: var(--paper); }
  .billboard {
    position: relative;
    width: 1200px;
    height: 357px;
    overflow: hidden;
    background: var(--paper);
  }
  .shapes { position: absolute; inset: 0; }
  .headline {
    position: absolute;
    left: 40px;
    top: 50px;
    font-family: "Bebas Neue", sans-serif;
    font-weight: 400;
    font-size: 120px;
    line-height: 93px;
    color: var(--brand-blue);
    letter-spacing: 1px;
    white-space: nowrap;
    transform: scaleX(0.88);
    transform-origin: left top;
  }
  .phone {
    position: absolute;
    left: 38px;
    top: 252px;
    font-family: "Montserrat", sans-serif;
    font-weight: 800;
    font-size: 74px;
    line-height: 90px;
    color: var(--ink-light);
    letter-spacing: -1px;
    white-space: nowrap;
  }
  .company-name {
    position: absolute;
    left: 574px;
    top: 256px;
    font-family: "Bebas Neue", sans-serif;
    font-size: 46px;
    line-height: 43px;
    color: var(--ink-light);
    white-space: nowrap;
  }
</style>
</head>
<body>
  <div class="billboard">
    <svg class="shapes" width="1200" height="357" viewBox="0 0 1200 357">
      <defs>
        <linearGradient id="photo-fill" x1="0" y1="0" x2="1" y2="1">
          <stop offset="0" stop-color="var(--photo-light)"/>
          <stop offset="1" stop-color="var(--photo-warm)"/>
        </linearGradient>
      </defs>
      <rect class="phone-band" x="0" y="245" width="811" height="112" fill="var(--brand-blue)"/>
      <polygon class="accent-stripe" points="650,0 713,0 851,112 851,357 811,357 811,128" fill="var(--brand-green)"/>
      <polygon class="porch-photo" role="img" aria-label="Photo of a covered screened porch with wicker lounge chairs, ceiling fans and a view of a lawn and lake" points="713,0 1200,0 1200,357 851,357 851,112" fill="url(#photo-fill)"/>
    </svg>

    <h1 class="headline">Your Screen<br>Porch Expert</h1>
    <p class="phone">555.214.0387</p>
    <p class="company-name">Harborview<br>Screening</p>
  </div>
</body>
</html>
```